Marlow Crest Group (Real Estate and Investment)

A high end, clean design.
We are a real estate company with sales, asset management and investment divisions. We want to use a black and white scheme which is really high end feel. The back of the card can just be the logo (black background with the white writing) as we will probably emboss this when we print)

Target Market(s)

High level investors, high end houses for sale

Industry/Entity Type

Business

Contact Information for Business Card

Name, position, phone number and email address
Glen Varley, Managing Director, 0437259064 and glen@marlowcrest-example.com.au

Requirements
Must have
• Back of the card to be the black background with the white writing (as per the attached images). Would like the capacity to emboss the writing and logo

```html
<!DOCTYPE html>
<html lang="en">
<head>
<meta charset="utf-8">
<title>Marlow Crest Group — Business Card</title>
<link rel="stylesheet" href="https://fonts.googleapis.com/css2?family=Arimo:wght@400;700&family=Raleway:wght@300&display=swap">
<style>
  :root {
    --ink: #111111;
    --paper: #ffffff;
    --backdrop: #ececec;
    --card-black: #0a0a0a;
    --muted: #333333;
  }
  * { box-sizing: border-box; margin: 0; padding: 0; }
  html, body {
    width: 1198px;
    height: 1200px;
    overflow: hidden;
    background: var(--backdrop);
  }
  .sheet {
    width: 1198px;
    height: 1200px;
    display: flex;
    flex-direction: column;
    align-items: center;
    justify-content: center;
    gap: 80px;
  }
  .card {
    width: 820px;
    height: 500px;
    position: relative;
    box-shadow: 0 6px 24px rgba(0,0,0,0.12);
  }
  .card--front { background: var(--paper); color: var(--ink); }
  .card--back { background: var(--card-black); color: var(--paper); }

  .brand {
    font-family: "Raleway", "Helvetica Neue", Arial, sans-serif;
    font-weight: 300;
    text-transform: uppercase;
    letter-spacing: 0.02em;
    white-space: nowrap;
  }
  .brand-mark {
    display: block;
    border: 2px solid currentColor;
    border-radius: 50%;
  }

  .card--front .brand-block {
    position: absolute;
    left: 80px;
    top: 150px;
    display: flex;
    flex-direction: column;
    align-items: center;
    gap: 34px;
    width: 300px;
  }
  .card--front .brand-mark { width: 120px; height: 120px; }
  .card--front .brand { font-size: 30px; }

  .contact {
    position: absolute;
    left: 450px;
    top: 70px;
    font-family: "Arimo", Arial, sans-serif;
    font-variant: small-caps;
  }
  .contact__name {
    font-size: 32px;
    font-weight: 700;
    letter-spacing: 0.01em;
  }
  .contact__role {
    font-size: 20px;
    color: var(--muted);
    margin-top: 4px;
  }
  .contact__list {
    list-style: none;
    margin-top: 56px;
    display: flex;
    flex-direction: column;
    gap: 14px;
  }
  .contact__item {
    display: flex;
    align-items: center;
    gap: 10px;
    font-size: 19px;
  }
  .contact__item--phone { font-size: 24px; }
  .contact__icon { width: 18px; height: 18px; flex: none; }

  .card--back .brand-block {
    position: absolute;
    right: 50px;
    bottom: 70px;
    display: flex;
    align-items: center;
    gap: 16px;
  }
  .card--back .brand-mark { width: 26px; height: 26px; }
  .card--back .brand { font-size: 30px; }
</style>
</head>
<body>
<main class="sheet">
  <section class="card card--front" aria-label="Card front">
    <div class="brand-block">
      <span class="brand-mark" aria-hidden="true"></span>
      <span class="brand">Marlow Crest Group</span>
    </div>
    <div class="contact">
      <p class="contact__name">Glen Varley</p>
      <p class="contact__role">Managing Director</p>
      <ul class="contact__list">
        <li class="contact__item contact__item--phone">
          <svg class="contact__icon" viewBox="0 0 18 18" aria-hidden="true"><rect x="4.5" y="1" width="9" height="16" rx="1.5" fill="none" stroke="currentColor" stroke-width="1.6"/><line x1="8" y1="14.5" x2="10" y2="14.5" stroke="currentColor" stroke-width="1.4"/></svg>
          043.725.9064
        </li>
        <li class="contact__item">
          <svg class="contact__icon" viewBox="0 0 18 18" aria-hidden="true"><rect x="1" y="4" width="16" height="11" fill="currentColor"/><polyline points="1,4 9,10 17,4" fill="none" stroke="#fff" stroke-width="1.2"/></svg>
          glen@marlowcrest-example.com.au
        </li>
        <li class="contact__item">
          <svg class="contact__icon" viewBox="0 0 18 18" aria-hidden="true"><circle cx="9" cy="9" r="8" fill="currentColor"/><g fill="none" stroke="#fff" stroke-width="1"><ellipse cx="9" cy="9" rx="3.5" ry="8"/><line x1="1" y1="9" x2="17" y2="9"/><line x1="2.5" y1="5" x2="15.5" y2="5"/><line x1="2.5" y1="13" x2="15.5" y2="13"/></g></svg>
          marlowcrest-example.com.au
        </li>
      </ul>
    </div>
  </section>

  <section class="card card--back" aria-label="Card back">
    <div class="brand-block">
      <span class="brand-mark" aria-hidden="true"></span>
      <span class="brand">Marlow Crest Group</span>
    </div>
  </section>
</main>
</body>
</html>
```